Optimising your students' achievement in PLQ English

The flyer is for an audience of English teachers in NSW, who are teaching PLQ English. We need a flyer that provides clear information about the services we can offer in terms of advice and professional learning for English teachers.
We are leading experts in this field and this is the first time we are offering tailored professional learning for individual schools and their English staff.
Attached is a document that provides details of the proposed content and inclusions (logos) for the flyer.

```html
<!DOCTYPE html>
<html lang="en">
<head>
<meta charset="utf-8">
<title>Optimising your students' achievement in PLQ English</title>
<link rel="stylesheet" href="https://fonts.googleapis.com/css2?family=Arimo:wght@400;700&family=Tinos:wght@700&display=swap">
<style>
  :root {
    --canvas-bg: #e9e7e2;
    --slate: #4f6479;
    --slate-dark: #3d4f62;
    --slate-light: #8597a9;
    --beige: #e7dec4;
    --beige-edge: #cfc3a2;
    --ink: #2a2a2a;
    --white: #ffffff;
    --brand-red: #b3212b;
  }
  * { box-sizing: border-box; margin: 0; padding: 0; }
  html, body { width: 1200px; height: 1000px; overflow: hidden; }
  body {
    background: var(--canvas-bg);
    font-family: "Arimo", Arial, sans-serif;
    color: var(--white);
  }
  .flyer {
    position: absolute;
    left: 290px; top: 20px;
    width: 620px; height: 960px;
    background: linear-gradient(180deg, var(--slate) 0%, var(--slate-dark) 100%);
    box-shadow: 0 6px 20px rgba(0,0,0,0.25);
    overflow: hidden;
  }
  .hero-photo {
    display: block;
    width: 620px; height: 230px;
  }
  .section-label {
    position: absolute; left: 24px; top: 242px;
    font-weight: 700; font-size: 16px;
  }
  .consultant {
    position: absolute;
    background: var(--beige);
    border: 1px solid var(--beige-edge);
    color: var(--ink);
    height: 118px;
    display: flex;
    align-items: flex-start;
    padding: 10px 14px;
    gap: 16px;
  }
  .consultant--first { left: 24px; top: 270px; width: 420px; }
  .consultant--second { right: 24px; top: 400px; width: 420px; }
  .portrait-block { width: 96px; flex: none; }
  .portrait { display: block; width: 96px; height: 76px; border: 2px solid var(--white); }
  .affiliation {
    display: flex; align-items: center; gap: 5px;
    margin-top: 4px;
    font-size: 10px; font-weight: 700; color: var(--brand-red);
  }
  .affiliation::before {
    content: ""; width: 9px; height: 9px; background: var(--brand-red); flex: none;
  }
  .consultant-name {
    font-family: "Tinos", "Times New Roman", serif;
    font-weight: 700; font-size: 21px; line-height: 1.05;
    margin-bottom: 6px;
  }
  .consultant-role { font-size: 11.5px; line-height: 1.35; }
  .support {
    position: absolute; left: 24px; top: 534px; width: 572px;
    font-size: 11.5px; line-height: 1.45;
  }
  .support h2 { font-size: 16px; font-weight: 700; margin-bottom: 6px; }
  .support p { margin-bottom: 6px; }
  .support-list { list-style: disc; padding-left: 18px; margin-bottom: 4px; }
  .support-list li { margin-bottom: 5px; }
  .workshop-list { list-style: circle; padding-left: 18px; }
  .workshop-list li { margin-bottom: 3px; }
  .contact-strip {
    position: absolute; left: 0; bottom: 0;
    width: 620px; height: 88px;
    background: var(--beige);
    color: var(--ink);
    font-size: 11.5px; line-height: 1.45;
    padding: 16px 24px;
  }
  .contact-strip strong { font-weight: 700; }
</style>
</head>
<body>
  <main class="flyer">
    <svg class="hero-photo" viewBox="0 0 620 230" role="img" aria-label="Photograph of five education professionals talking together outside a building">
      <defs>
        <linearGradient id="heroTone" x1="0" y1="0" x2="1" y2="1">
          <stop offset="0" stop-color="#b9c2c9"/>
          <stop offset="0.45" stop-color="#5d6671"/>
          <stop offset="0.8" stop-color="#c79a5a"/>
          <stop offset="1" stop-color="#6f8f55"/>
        </linearGradient>
      </defs>
      <rect width="620" height="230" fill="url(#heroTone)"/>
    </svg>

    <div class="section-label">Consultants:</div>

    <section class="consultant consultant--first">
      <div class="portrait-block">
        <svg class="portrait" viewBox="0 0 96 76" role="img" aria-label="Portrait photo of Associate Professor Helena Marsh">
          <rect width="96" height="76" fill="#8fa6c0"/>
        </svg>
        <div class="affiliation">Harbourview</div>
      </div>
      <div>
        <h3 class="consultant-name">Associate Professor<br>Helena Marsh</h3>
        <p class="consultant-role">Harbourview University<br>Chief Examiner, PLQ English<br>(Standard and Advanced, 2008–2011)</p>
      </div>
    </section>

    <section class="consultant consultant--second">
      <div class="portrait-block">
        <svg class="portrait" viewBox="0 0 96 76" role="img" aria-label="Portrait photo of Dr Neil Porter">
          <rect width="96" height="76" fill="#4e6c96"/>
        </svg>
        <div class="affiliation">SCI</div>
      </div>
      <div>
        <h3 class="consultant-name">Dr Neil Porter</h3>
        <p class="consultant-role">Southern Cross Institute<br>Former Inspector, English at the<br>State Board of Curriculum, Teaching<br>and Educational Standards</p>
      </div>
    </section>

    <section class="support">
      <h2>How we can support you:</h2>
      <p>School-based professional learning for Stage 6 English teachers with leading experts in PLQ English and examinations.</p>
      <p>We will work with you and your staff to:</p>
      <ul class="support-list">
        <li>Plan and/or provide advice on all aspects of Stage 6 English courses</li>
        <li>Provide tailored professional learning to assist Stage 6 English teachers in raising students' achievement in PLQ English examinations, with learning designed around your needs to build sustained collaboration with your staff</li>
        <li>Provide targeted workshops in:</li>
      </ul>
      <ul class="workshop-list">
        <li>Preparing your students for PLQ English examinations: what they need to know to succeed in English examinations</li>
        <li>Teaching and learning strategies specifically focused on building examination technique and confidence</li>
        <li>Successfully planning, programming, teaching and resourcing Stage 6 English</li>
        <li>Research-based strategies and a coherent approach to pedagogy for developing students' writing abilities in PLQ English examinations</li>
      </ul>
    </section>

    <footer class="contact-strip">
      To discuss your professional learning requirements or for more information, please contact Helena (<strong>helena.marsh@harbourview.edu.au</strong>) or Neil (<strong>neil.porter@scinstitute.edu.au</strong>) and we will be happy to talk with you about any aspect of your Stage 6 English teaching.
    </footer>
  </main>
</body>
</html>
```